Health Care Service Company Flyer

Company name: Bright Harbor Clinic
Slogan: Find out what you're made of
Website: brightharborclinic.ca

I need the flyer to contain the company name (will provide logo source file ASAP), the slogan in large font and a "find out more at harborclinic.ca"

Other important data to include in the flyer is:
Four bullet points with the following information:
*Track performance and fitness results over time
*Develop proprietary exercise and dietary programs based on actionable data
*Track muscle atrophy from injury, as well as muscle gain during rehabilitation
*Reveal imbalances in muscle symmetry and strength, flexibility, and joint mechanics

I also need the following information conveyed somewhere on the flyer:
*Body Fat, Muscle Mass, and Bone Density Measurements
• Over 50 data points generated in each 10 minute scan
*Call XXX-XXX-XXX to book an appointment today

DEXA Body Composition Services.
Get scanned today.

See example of competitor flyers in the images to get an example of the images and information we are trying to convey

Target Market(s)

athletes, fitness enthusiast, crossfit

Industry/Entity Type

Health And Wellness

Colors
33a6d7
acd036

Requirements
Nice to have
• Prefer images be general health and wellness related - in other words, individuals who look healthy, but are not abnormally muscular
Should not have
• Shirtless models, No big muscles,

```html
<!DOCTYPE html>
<html lang="en">
<head>
<meta charset="utf-8">
<title>Bright Harbor Clinic – Flyer</title>
<link rel="stylesheet" href="https://fonts.googleapis.com/css2?family=Bebas+Neue&family=Montserrat:wght@400;500;700&display=swap">
<style>
  :root {
    --brand-blue: #33a6d7;
    --brand-green: #acd036;
    --ink-dark: #0c1016;
    --ink-panel: #141a21;
    --paper: #ffffff;
    --text-light: #f2f4f6;
    --text-dark: #111111;
    --stage: #d9dbde;
  }
  * { margin: 0; padding: 0; box-sizing: border-box; }
  html, body { width: 1200px; height: 1200px; overflow: hidden; }
  body { background: var(--stage); position: relative; font-family: "Montserrat", sans-serif; }

  .flyer {
    position: absolute; left: 204px; top: 39px;
    width: 792px; height: 1122px;
    background: var(--ink-dark);
    overflow: hidden;
  }
  .flyer-shapes { position: absolute; inset: 0; }

  .brand-name {
    position: absolute; left: 35px; top: 58px;
    font-family: "Bebas Neue", sans-serif;
    font-size: 58px; line-height: 1; letter-spacing: 0.5px;
    color: var(--brand-blue);
  }

  .headline {
    position: absolute; left: 33px; top: 338px;
    font-family: "Bebas Neue", sans-serif;
    line-height: 0.86;
  }
  .headline span { display: block; }
  .headline .line-lead { font-size: 120px; color: var(--brand-blue); }
  .headline .line-mid { font-size: 82px; color: var(--brand-green); margin: 2px 0 6px; }
  .headline .line-end { font-size: 120px; color: var(--brand-blue); }

  .measures {
    position: absolute; left: 37px; top: 642px; width: 315px; height: 106px;
    border-top: 1.5px solid #c9ced4; border-bottom: 1.5px solid #c9ced4;
  }
  .measure {
    position: absolute; display: flex; align-items: flex-start; gap: 7px;
    color: var(--text-light); font-size: 15px; line-height: 19px; letter-spacing: 0.3px;
  }
  .measure svg { flex: none; margin-top: -7px; }
  .measure.body-fat { left: 2px; top: 18px; }
  .measure.muscle-mass { left: 2px; top: 64px; }
  .measure.bone-density { left: 153px; top: 18px; }

  .scan-badge {
    position: absolute; left: 88px; top: 785px;
    width: 234px; height: 234px; border-radius: 50%;
    background: var(--paper);
    border: 11px solid #8fb21f;
    display: flex; flex-direction: column; align-items: center; justify-content: center;
    font-family: "Bebas Neue", sans-serif;
    font-size: 35px; line-height: 39px; color: var(--text-dark);
  }
  .scan-badge .accent { color: #1d7fb8; }

  .benefits {
    position: absolute; right: 50px; top: 731px; width: 400px;
    list-style: none; text-align: right;
    color: var(--text-light); font-size: 17.5px; line-height: 23px; letter-spacing: 0.2px;
  }
  .benefits li { position: relative; padding-right: 26px; margin-bottom: 9px; }
  .benefits li svg { position: absolute; right: -3px; top: 4px; }

  .booking {
    position: absolute; right: 38px; top: 1041px; text-align: right;
    color: var(--text-light); font-weight: 700;
  }
  .booking .call { font-size: 29px; line-height: 34px; letter-spacing: 0.5px; }
  .booking .call .phone { color: var(--brand-green); }
  .booking .book { font-size: 16.5px; letter-spacing: 0.6px; }

  .website {
    position: absolute; left: 108px; top: 1073px;
    color: var(--brand-blue); font-size: 17px; letter-spacing: 2px;
  }
</style>
</head>
<body>
  <main class="flyer">
    <svg class="flyer-shapes" width="792" height="1122" viewBox="0 0 792 1122">
      <defs>
        <radialGradient id="photo-tone" cx="0.6" cy="0.45" r="0.7">
          <stop offset="0" stop-color="#c99a7c"/>
          <stop offset="0.45" stop-color="#6e5a52"/>
          <stop offset="1" stop-color="#161b22"/>
        </radialGradient>
      </defs>
      <rect class="lower-panel" x="0" y="707" width="792" height="415" fill="#171d25"/>
      <polygon class="hero-photo" role="img" aria-label="Photo of a smiling woman in a grey sports top lifting a blue dumbbell"
        points="360,40 792,40 792,512 696,642 646,707 411,707 360,758"
        fill="url(#photo-tone)"/>
      <polygon class="header-panel" points="0,0 552,0 381,174 136,174 0,312" fill="#ffffff"/>
      <polyline class="header-rule" points="470,85 381,174 136,174 0,312" fill="none" stroke="#33a6d7" stroke-width="6"/>
      <polygon class="accent-bar" points="512,0 562,0 478,88 462,63" fill="#acd036"/>
      <polygon class="accent-bar" points="0,282 88,196 98,222 0,318" fill="#acd036"/>
      <polyline class="section-rule" points="296,822 411,707 646,707 696,642" fill="none" stroke="#33a6d7" stroke-width="6"/>
      <polygon class="accent-bar" points="696,615 792,510 792,548 708,660" fill="#acd036"/>
      <polygon class="accent-bar" points="0,1086 146,968 158,1000 0,1122" fill="#acd036"/>
    </svg>

    <div class="brand-name">BRIGHT HARBOR CLINIC</div>

    <h1 class="headline">
      <span class="line-lead">FIND OUT</span>
      <span class="line-mid">WHAT YOU'RE</span>
      <span class="line-end">MADE OF</span>
    </h1>

    <div class="measures">
      <div class="measure body-fat">
        <svg width="33" height="33" viewBox="0 0 33 33"><circle cx="16.5" cy="16.5" r="15.5" fill="none" stroke="#f2f4f6" stroke-width="1.2"/><path d="M11 10 q5.5 4 11 0 v13 h-11z M14 16 h5" fill="none" stroke="#f2f4f6" stroke-width="1.3"/></svg>
        <span>Body Fat</span>
      </div>
      <div class="measure muscle-mass">
        <svg width="33" height="33" viewBox="0 0 33 33"><circle cx="16.5" cy="16.5" r="15.5" fill="none" stroke="#f2f4f6" stroke-width="1.2"/><path d="M9 22 q3-10 8-11 q3 0 2 4 q5 0 6 5 q-6 3-16 2z" fill="none" stroke="#f2f4f6" stroke-width="1.3"/></svg>
        <span>Muscle Mass</span>
      </div>
      <div class="measure bone-density">
        <svg width="33" height="33" viewBox="0 0 33 33"><circle cx="16.5" cy="16.5" r="15.5" fill="none" stroke="#f2f4f6" stroke-width="1.2"/><path d="M13 9 v15 M17 9 v15 M13 12 h4 M13 16 h4 M13 20 h4 M20 10 q4 2 0 5" fill="none" stroke="#f2f4f6" stroke-width="1.3"/></svg>
        <span>Bone<br>Density<br>Measurement</span>
      </div>
    </div>

    <div class="scan-badge">
      <span>OVER</span>
      <span><span class="accent">50 DATA</span> POINTS</span>
      <span>GENERATED IN EACH</span>
      <span><span class="accent">10 MINUTE</span> SCAN</span>
    </div>

    <ul class="benefits">
      <li>Track performance and fitness<br>results over time<svg width="13" height="13" viewBox="0 0 13 13"><rect x="0.7" y="0.7" width="11.6" height="11.6" fill="none" stroke="#acd036" stroke-width="1.3"/><path d="M3 6.5 l2.5 2.5 l5-6" fill="none" stroke="#acd036" stroke-width="1.5"/></svg></li>
      <li>Develop proprietary exercise &amp;<br>dietary programs based on<br>actionable data<svg width="13" height="13" viewBox="0 0 13 13"><rect x="0.7" y="0.7" width="11.6" height="11.6" fill="none" stroke="#acd036" stroke-width="1.3"/><path d="M3 6.5 l2.5 2.5 l5-6" fill="none" stroke="#acd036" stroke-width="1.5"/></svg></li>
      <li>Track muscle atrophy from injury,<br>as well as muscle gain during<br>rehabilitation<svg width="13" height="13" viewBox="0 0 13 13"><rect x="0.7" y="0.7" width="11.6" height="11.6" fill="none" stroke="#acd036" stroke-width="1.3"/><path d="M3 6.5 l2.5 2.5 l5-6" fill="none" stroke="#acd036" stroke-width="1.5"/></svg></li>
      <li>Reveal imbalances in muscle<br>symmetry and strength, flexibility,<br>and joint mechanics<svg width="13" height="13" viewBox="0 0 13 13"><rect x="0.7" y="0.7" width="11.6" height="11.6" fill="none" stroke="#acd036" stroke-width="1.3"/><path d="M3 6.5 l2.5 2.5 l5-6" fill="none" stroke="#acd036" stroke-width="1.5"/></svg></li>
    </ul>

    <div class="booking">
      <div class="call">CALL <span class="phone">XXX-XXX-XXX</span></div>
      <div class="book">TO BOOK AN APPOINTMENT TODAY</div>
    </div>

    <div class="website">www.brightharborclinic.ca</div>
  </main>
</body>
</html>
```